Flyer Design

I need a flyer to advertise my
home parties for hens night and girls nights
we offer free parties and premium parties from $149
needed to hand out at other parties and in orders.
I have a logo and would like to include a pic or 2
colours mainly black and pinks.
Mainly letting customers know what we offer, packages,
how to book, and an offer for booking now.

Target Market(s)

women 18+

Requirements
Must have
• Details include but words can be changed to suit-
Free home parties, party games and novelties, Cheeky Evenings photo booth, And male entertainers
loads of host and hens gifts
games and trivia lots to choose from with
adult toys lingerie costumes corsets
book at www.velvetandglow.example
or 0482570914
book today and get a upgrade to premium games prize pack $50 value+

Nice to have
• make me want to book a party, you can be creative.

```html
<!DOCTYPE html>
<html lang="en">
<head>
<meta charset="utf-8">
<title>Velvet &amp; Glow – Home Party Flyer</title>
<link rel="stylesheet" href="https://fonts.googleapis.com/css2?family=Tinos:ital,wght@0,700;1,700&display=swap">
<style>
  :root {
    --ink: #0b0b0b;
    --night: #141414;
    --blush: #f4cfdc;
    --blush-soft: #f0d3dc;
    --blush-deep: #e6c3cf;
    --band-edge: #3a3a3a;
    --brand-ink: #1c1c1c;
    --glow: rgba(255, 255, 255, 0.35);
    --shade: rgba(0, 0, 0, 0.85);
  }
  html, body {
    margin: 0;
    padding: 0;
    overflow: hidden;
    background: var(--ink);
  }
  .flyer {
    position: relative;
    width: 851px;
    height: 1200px;
    overflow: hidden;
    background: radial-gradient(ellipse at 50% 40%, var(--night) 0%, var(--ink) 75%);
    font-family: "Tinos", "Times New Roman", serif;
  }
  .offer-list,
  .booking {
    position: absolute;
    left: 0;
    width: 100%;
    margin: 0;
    padding: 0;
    list-style: none;
    text-align: center;
  }
  .offer-list { top: 39px; }
  .booking { top: 916px; }
  .offer-list li,
  .booking p {
    margin: 0;
    height: 57.4px;
    line-height: 57.4px;
    font-size: 38px;
    font-weight: 700;
    font-style: italic;
    color: var(--blush);
    text-shadow: 0 0 4px var(--glow), 2px 2px 3px var(--shade);
    white-space: nowrap;
  }
  .brand-band {
    position: absolute;
    left: 0;
    top: 575px;
    width: 851px;
    height: 186px;
    background: linear-gradient(90deg,
      var(--band-edge) 0%, var(--blush-soft) 9%,
      var(--blush-soft) 88%, var(--band-edge) 100%);
  }
  .brand-disc {
    position: absolute;
    left: 245px;
    top: 505px;
    width: 360px;
    height: 360px;
    border-radius: 50%;
    background: var(--blush-deep);
  }
  .brand-name {
    position: absolute;
    left: 245px;
    top: 546px;
    width: 360px;
    margin: 0;
    text-align: center;
    font-family: "Tinos", "Times New Roman", serif;
    font-weight: 700;
    font-style: normal;
    font-size: 78px;
    line-height: 92px;
    color: var(--brand-ink);
  }
  .brand-name span { display: block; }
</style>
</head>
<body>
  <main class="flyer">
    <ul class="offer-list">
      <li>Free home parties</li>
      <li>Party games and novelties</li>
      <li>Cheeky Evenings photo booth</li>
      <li>Male entertainers</li>
      <li>With</li>
      <li>Loads of host and hens gifts</li>
      <li>games and trivia lots to choose from with adult</li>
      <li>toys lingerie costumes corsetst</li>
    </ul>

    <div class="brand-band"></div>
    <div class="brand-disc"></div>
    <h1 class="brand-name"><span>Velvet</span><span>&amp;</span><span>Glow</span></h1>

    <section class="booking">
      <p>book at</p>
      <p>www.velvetandglow.example or 0482570914</p>
      <p>book today and get a upgrade to premium games</p>
      <p>prize pack $50 value+</p>
    </section>
  </main>
</body>
</html>
```